TALLOW RIDGE BUILDERS leave behind sales FLYER 8.5"x11"

We need a high quality advertising flyer 8.5"x11" for our construction company offering kitchen and bathroom remodels. Can be front and back or just the front of the flyer depending on the design. phone number to come
www.brennikhomeworks.com

we are also a home inspection company. We will leave this at the home when we are done with our home inspections for our new home owners

Target Market(s)

Home owners

Industry/Entity Type

Residential Construction

Contact Information for Business Card

We want it to match the flyer please

Requirements
Must have
• My logo, my website , my phone number (to come later),
• FL State Lic. #CRC8841739 & Insured
• We Specialize in Bathroom and Kitchen remodeling ,new Construction & Interior or Exterior home Renovations, garages and more! Serving Central Florida for over 15 years.
• Family owned and operated,
• we perform all levels of building and remodeling.
• i wouldn't mind seeing what you come up with for text on the flyer.
Nice to have
• maybe a nice kitchen and bathroom pictures

```html
<!DOCTYPE html>
<html lang="en">
<head>
<meta charset="utf-8">
<title>Tallow Ridge Builders – Flyer</title>
<link rel="stylesheet" href="https://fonts.googleapis.com/css2?family=Montserrat:wght@400;500;600;700&family=Poppins:wght@300;400;500&display=swap">
<style>
  :root {
    --orange: #f7931e;
    --orange-soft: #f9a74a;
    --ink: #111111;
    --grey: #4a4a4a;
    --brand-grey: #555555;
    --paper: #ffffff;
    --footer: #000000;
  }
  * { margin: 0; padding: 0; box-sizing: border-box; }
  html, body { width: 927px; height: 1200px; overflow: hidden; background: var(--paper); }
  .flyer { position: relative; width: 927px; height: 1200px; background: var(--paper); overflow: hidden; font-family: "Poppins", sans-serif; }

  .brand { position: absolute; left: 150px; top: 66px; width: 190px; text-align: center; }
  .brand-mark { width: 78px; height: 78px; background: var(--orange); margin: 0 auto 14px; }
  .brand-name { font-family: "Montserrat", sans-serif; font-weight: 600; color: var(--brand-grey); font-size: 22px; letter-spacing: 3px; line-height: 1.3; }

  .website { position: absolute; left: 527px; top: 46px; font-family: "Montserrat", sans-serif; font-weight: 500; font-size: 22px; color: var(--ink); }

  .frame { position: absolute; background: var(--orange); }
  .photo { position: absolute; }
  .photo-kitchen { left: 379px; top: 73px; width: 412px; height: 275px;
    background: linear-gradient(160deg, #e9dcc0 0%, #cfb58c 45%, #8f6a44 100%); }
  .photo-bath { left: 56px; top: 250px; width: 433px; height: 280px;
    background: linear-gradient(120deg, #6f8a92 0%, #9fb3b6 35%, #eef0ee 70%, #d9d9d6 100%); }
  .photo-modern { left: 485px; top: 326px; width: 371px; height: 280px; border: 6px solid var(--paper);
    background: linear-gradient(170deg, #f3f3f1 0%, #e2e0dc 55%, #a8744a 100%); }

  .services-panel { position: absolute; left: 614px; top: 700px; width: 313px; height: 391px;
    background: linear-gradient(180deg, rgba(249,167,74,0) 0%, rgba(249,167,74,0.55) 45%, var(--orange-soft) 100%); }

  .headline { position: absolute; left: 56px; top: 556px; font-family: "Montserrat", sans-serif; color: var(--ink); line-height: 1.18; }
  .headline-line { display: block; font-size: 45px; font-weight: 500; }
  .headline-accent { display: block; font-size: 49px; font-weight: 700; color: var(--orange); }

  .intro { position: absolute; left: 60px; top: 741px; width: 540px; font-weight: 300; font-size: 22px; line-height: 38.5px; color: var(--grey); }

  .services { position: absolute; left: 648px; top: 748px; }
  .services-title { font-family: "Montserrat", sans-serif; font-weight: 500; font-size: 27px; letter-spacing: 1px; color: var(--ink); margin-bottom: 6px; }
  .services-list { list-style: none; }
  .services-list li { position: relative; padding-left: 36px; font-size: 18.5px; line-height: 30.3px; color: var(--ink); }
  .services-list li::before { content: ""; position: absolute; left: 4px; top: 13px; width: 6px; height: 6px; border-radius: 50%; background: var(--ink); }

  .footer { position: absolute; left: 0; top: 1091px; width: 927px; height: 109px; background: var(--footer); }
  .license { position: absolute; left: 56px; top: 1129px; font-size: 17px; color: var(--orange); }
  .phone { position: absolute; right: 51px; top: 1108px; font-family: "Montserrat", sans-serif; font-weight: 600; font-size: 38px; letter-spacing: 3px; color: var(--orange); }
</style>
</head>
<body>
<main class="flyer">
  <div class="brand">
    <div class="brand-mark"></div>
    <div class="brand-name">TALLOW RIDGE<br>BUILDERS</div>
  </div>

  <div class="website">www.brennikhomeworks.com</div>

  <div class="frame" style="left:361px;top:53px;width:162px;height:11px;"></div>
  <div class="frame" style="left:361px;top:53px;width:11px;height:145px;"></div>
  <div class="photo photo-kitchen" role="img" aria-label="Bright kitchen with cream cabinets, granite counters and a dining area"></div>

  <div class="photo photo-bath" role="img" aria-label="Classic bathroom with blue walls, white tub, pedestal sink and tiled floor"></div>
  <div class="frame" style="left:56px;top:530px;width:368px;height:12px;"></div>

  <div class="frame" style="left:803px;top:288px;width:73px;height:11px;"></div>
  <div class="frame" style="left:865px;top:288px;width:11px;height:170px;"></div>
  <div class="photo photo-modern" role="img" aria-label="Modern white kitchen with wood cabinetry and pendant lights"></div>

  <div class="services-panel"></div>

  <h1 class="headline">
    <span class="headline-line">WE GUARANTEE</span>
    <span class="headline-accent">HIGH-QUALITY CONSTRUCTION</span>
    <span class="headline-line">FOR EACH AND EVERY PROJECT.</span>
  </h1>

  <p class="intro">Family owned and operated, we perform all levels of building and remodeling. We offer start-to-finish solutions for every project. We specialize in interior or exterior home renovations, including bathroom and kitchen remodeling, home additions, garages and more! Serving Central Florida for over 15 years.</p>

  <section class="services">
    <h2 class="services-title">Our Services</h2>
    <ul class="services-list">
      <li>New Construction</li>
      <li>Barns</li>
      <li>Remodels</li>
      <li>Renovations</li>
      <li>Repairs</li>
      <li>Kitchens</li>
      <li>Bathrooms</li>
      <li>Bank Remodels</li>
    </ul>
  </section>

  <footer class="footer"></footer>
  <div class="license">FL State Lic. #CRC8841739 &amp; Insured</div>
  <div class="phone">352-555-0186</div>
</main>
</body>
</html>
```